Webdesign for an Health & Beauty Center

We need a new modern and elegant web design for the relaunch of the http://veskarin.at/ website.
The website is for a company which offer all services for a beuty center like epilation, cosmetics and more.
The new website should use big emotional background images and a modern menu.
All in all the website should give a female expression and the design should be clear and not playful.
The existing logo used be used for the new design, the base colours of the existing website could be used optionally.

Reason: Review of the designs together with the customer needs a little more time.

Industry/Entity Type
It Company
Look and feel
Each slider illustrates characteristics of the customer's brand and the style your logo design should communicate.

```html
<!DOCTYPE html>
<html lang="en">
<head>
<meta charset="utf-8">
<title>Veskarin – Health & Beauty Center</title>
<link href="https://fonts.googleapis.com/css2?family=Lato:wght@300;400;700&family=Poiret+One&display=swap" rel="stylesheet">
<style>
:root{
  --gold:#c8b07e;
  --gold-text:#d3b98a;
  --nav:#c4a888;
  --nav-active:#e9a46a;
  --grey-title:#b7b9c6;
  --grey-text:#c3c5cd;
  --sunday:#a8aebb;
  --footer:#383e4a;
  --footer-field:#2f3440;
  --footer-head:#8d93a0;
  --footer-text:#5f6675;
  --white:#ffffff;
}
*{margin:0;padding:0;box-sizing:border-box}
html,body{width:771px;height:1200px;overflow:hidden;background:var(--white)}
body{position:relative;font-family:'Lato',sans-serif;font-weight:300}
.abs{position:absolute}
.logo-name{left:118px;top:14px;font-family:'Lato',sans-serif;font-weight:300;font-size:26px;letter-spacing:4px;color:var(--gold)}
.logo-tag{left:146px;top:55px;font-size:7.5px;letter-spacing:1.2px;color:#8c8a86;font-weight:400}
.nav{top:37px;display:flex;gap:0;font-size:7.5px;color:var(--nav);font-weight:400}
.nav span{position:absolute;white-space:nowrap}
.hero{left:0;top:84px;width:771px;height:260px;background:linear-gradient(90deg,#f3ead8 0%,#f6e7c9 35%,#f0dcbf 55%,#d7e9df 85%,#bfdccf 100%)}
.cap-title{left:118px;top:177px;width:168px;height:24px;background:rgba(200,176,126,.85);color:#fff;font-size:8.5px;font-weight:700;padding:7px 10px}
.cap-body{left:118px;top:209px;width:260px;height:37px;background:rgba(200,176,126,.85);color:#fff;font-size:6.8px;line-height:10px;padding:4px 10px}
.arrow{width:17px;height:17px;border-radius:50%;background:#fff;display:flex;align-items:center;justify-content:center}
.dot{width:8px;height:8px;border-radius:50%;border:1px solid #fff;top:330px}
.decor{left:360px;top:344px;width:411px;height:460px;background:radial-gradient(ellipse at 55% 40%,rgba(236,228,222,.75) 0%,rgba(243,238,235,.5) 45%,rgba(255,255,255,0) 75%)}
.sec-title{left:0;width:771px;text-align:center;font-size:15px;color:var(--grey-title);font-weight:300}
.rule{left:369px;width:33px;height:1px;background:var(--gold)}
.day{top:441px;width:70px;height:48px;background:var(--gold);color:#fff;font-size:13px;font-weight:400;display:flex;align-items:center;justify-content:center;letter-spacing:-.3px}
.day.sun{background:var(--sunday)}
.hours{top:499px;width:70px;text-align:center;font-size:7.5px;color:var(--grey-text)}
.svc-img{top:613px;width:169px;height:96px}
.svc-name{top:722px;width:169px;text-align:center;font-size:9.5px;color:var(--gold-text);font-weight:400}
.svc-text{top:742px;width:169px;text-align:center;font-size:6.6px;line-height:11.5px;color:var(--grey-text)}
.avatar{left:118px;top:895px;width:24px;height:24px;border-radius:50%;background:#9a7a5e}
.client{left:152px;font-size:7.5px;color:var(--grey-text)}
.quote{left:214px;top:885px;width:435px;text-align:center;font-size:8.3px;line-height:14.5px;color:var(--grey-text)}
.qmark{font-family:Georgia,serif;font-size:20px;font-weight:700;color:#b2b6c2}
.tbtn{top:950px;width:14px;height:14px;background:var(--sunday);display:flex;align-items:center;justify-content:center}
.footer{left:0;top:1012px;width:771px;height:188px;background:var(--footer)}
.f-head{top:1029px;font-size:10px;color:var(--footer-head);font-weight:400}
.f-text{font-size:6.3px;line-height:10.2px;color:var(--footer-text)}
.thumb{width:37px;height:36px}
.soc{top:1122px;width:14px;height:14px;background:#454b58}
.field{background:var(--footer-field);font-size:6.3px;color:#6d7380;padding:4px 7px}
.send{left:484px;top:1140px;width:57px;height:17px;background:var(--footer-field);color:#6d7380;font-size:7px;text-align:center;line-height:17px}
.f-rule{left:118px;top:1185px;width:535px;height:1px;background:#4a505c}
.copy{left:118px;top:1189px;font-size:6px;color:var(--footer-text)}
</style>
</head>
<body>
<header>
  <div class="abs logo-name">veskarin</div>
  <div class="abs logo-tag">HEALTH &amp; BEAUTY CENTER</div>
  <nav class="abs nav" style="left:0">
    <span style="left:351px;color:var(--nav-active)">Home</span>
    <span style="left:383px">About us</span>
    <span style="left:426px">Services</span>
    <span style="left:466px">Gallery</span>
    <span style="left:503px">Care line</span>
    <span style="left:546px">Offers</span>
    <span style="left:580px">Price lists</span>
    <span style="left:625px">Contact</span>
  </nav>
</header>

<section>
  <div class="abs hero" role="img" aria-label="Smiling woman with windswept blonde hair on a soft mint background"></div>
  <div class="abs cap-title">Praesent pellentesque blandit turpis</div>
  <div class="abs cap-body">Integer mi quam, pellentesque quis velit id, tincidunt molestie felis. Quisque a erat nec ipsum dictum lobortis sed id massa. Integer dictum lobortis libero, in pellentesque erat congue at.</div>
  <div class="abs arrow" style="left:53px;top:206px"><svg width="6" height="6" viewBox="0 0 6 6"><path d="M4 0.5 1.5 3 4 5.5" fill="none" stroke="#c8b07e" stroke-width="1"/></svg></div>
  <div class="abs arrow" style="left:701px;top:206px"><svg width="6" height="6" viewBox="0 0 6 6"><path d="M2 0.5 4.5 3 2 5.5" fill="none" stroke="#c8b07e" stroke-width="1"/></svg></div>
  <div class="abs dot" style="left:368px;background:#fff"></div>
  <div class="abs dot" style="left:382px"></div>
  <div class="abs dot" style="left:394px"></div>
</section>

<div class="abs decor" role="img" aria-label="Faint backdrop of a woman with long flowing hair"></div>

<section>
  <h2 class="abs sec-title" style="top:388px">Opening Time</h2>
  <div class="abs rule" style="top:415px"></div>
  <div class="abs day" style="left:118px">MON.</div>
  <div class="abs day" style="left:196px">TUE.</div>
  <div class="abs day" style="left:273px">WED.</div>
  <div class="abs day" style="left:351px">THU.</div>
  <div class="abs day" style="left:428px">FRI.</div>
  <div class="abs day" style="left:506px">SAT.</div>
  <div class="abs day sun" style="left:583px">SUN.</div>
  <div class="abs hours" style="left:118px">9:00 - 19:00</div>
  <div class="abs hours" style="left:196px">9:00 - 19:00</div>
  <div class="abs hours" style="left:273px">9:00 - 19:00</div>
  <div class="abs hours" style="left:351px">9:00 - 19:00</div>
  <div class="abs hours" style="left:428px">9:00 - 19:00</div>
  <div class="abs hours" style="left:506px">9:00 - 01:00</div>
  <div class="abs hours" style="left:583px">Closed</div>
</section>

<section>
  <h2 class="abs sec-title" style="top:561px">Our Services</h2>
  <div class="abs rule" style="top:588px"></div>
  <div class="abs svc-img" style="left:118px;background:linear-gradient(135deg,#2a2128,#4a3a40 50%,#6e3a6a)" role="img" aria-label="Make-up artist applying eye shadow with a brush"></div>
  <div class="abs svc-img" style="left:301px;background:linear-gradient(135deg,#f6d8c2,#f0b98f 50%,#fbeee4)" role="img" aria-label="Wax strip epilation on a leg"></div>
  <div class="abs svc-img" style="left:484px;background:linear-gradient(135deg,#b9753f,#d99a5e 50%,#f3e2cf)" role="img" aria-label="Woman receiving a back massage with candles"></div>
  <div class="abs svc-name" style="left:118px">Make-up</div>
  <div class="abs svc-name" style="left:301px">Epilation</div>
  <div class="abs svc-name" style="left:484px">Massage</div>
  <p class="abs svc-text" style="left:118px">Donec dictum sollicitudin ligula id molestie. Etiam ultricies nisl a lobortis varius. Etiam ullam-corper, turpis eu tincidunt laoreet, tellus nulla elementum arcu, quis tincidunt.</p>
  <p class="abs svc-text" style="left:301px">Nam bibendum rutrum nisl. Proin sit amet lorem ac tortor ornare vulputate. Nullam molestie ipsum ut mauris suscipit, in dapibus nisl luctus. Nam commodo semper pretium.</p>
  <p class="abs svc-text" style="left:484px">Duis dapibus iaculis facilisis. Curabitur facilisis ligula vitae iaculis volutpat. Integer rhoncus enim non dui dictum pretium. Duis fringilla, massa vul-putate feugiat tincidunt.</p>
</section>

<section>
  <h2 class="abs sec-title" style="top:838px">Testimonials</h2>
  <div class="abs rule" style="top:865px"></div>
  <div class="abs avatar" role="img" aria-label="Client portrait"></div>
  <div class="abs client" style="top:897px">Marla</div>
  <div class="abs client" style="top:909px">Client</div>
  <span class="abs qmark" style="left:214px;top:872px">&ldquo;</span>
  <p class="abs quote">Duis dapibus iaculis facilisis curabitur facilisis ligula vitae iaculis volutpat. Integer rhoncus enim non dui dictum pretium, duis fringilla, massa vulputate feugiat tincidunt, turpis neque venenatis nulla, molestie tincidunt elit enim faucibus lacus. Nunc augue enim, convallis vitae auctor ut, ullamcorper posuere felis.</p>
  <span class="abs qmark" style="left:614px;top:914px">&rdquo;</span>
  <div class="abs tbtn" style="left:622px"><svg width="6" height="6" viewBox="0 0 6 6"><path d="M4 0.5 1.5 3 4 5.5" fill="none" stroke="#fff" stroke-width="1.2"/></svg></div>
  <div class="abs tbtn" style="left:639px"><svg width="6" height="6" viewBox="0 0 6 6"><path d="M2 0.5 4.5 3 2 5.5" fill="none" stroke="#fff" stroke-width="1.2"/></svg></div>
</section>

<footer>
  <div class="abs footer"></div>
  <h3 class="abs f-head" style="left:118px">About Us</h3>
  <h3 class="abs f-head" style="left:255px">Gallery</h3>
  <h3 class="abs f-head" style="left:346px">Get in touch</h3>
  <h3 class="abs f-head" style="left:484px">Contact us</h3>
  <p class="abs f-text" style="left:118px;top:1055px;width:122px">Duis dapibus iaculis facilisis curabitur facilisis ligula vitae iaculis volutpat. Inte-ger rhoncus enim non dui dictum pretium, duis fringilla, massa vulputate feugiat tincidunt, turpis neque venenatis nulla, molestie tincidunt elit enim faucibus lacus.</p>
  <p class="abs f-text" style="left:118px;top:1132px;width:122px">Nunc augue enim, convallis vitae auctor ut, ullamcorper posuere felis.</p>
  <div class="abs thumb" style="left:255px;top:1058px;background:#c98a8e" role="img" aria-label="Manicured nails"></div>
  <div class="abs thumb" style="left:296px;top:1058px;background:#efb995" role="img" aria-label="Epilation treatment"></div>
  <div class="abs thumb" style="left:255px;top:1098px;background:#3a2d30" role="img" aria-label="Make-up session"></div>
  <div class="abs thumb" style="left:296px;top:1098px;background:#d86aa4" role="img" aria-label="Styled portrait"></div>
  <p class="abs f-text" style="left:347px;top:1055px;width:120px">Veskarin - Health &amp; Beauty Center<br>218 Linden Court, Suite B4<br>Graz 8010</p>
  <p class="abs f-text" style="left:347px;top:1090px;width:130px">
    <svg width="6" height="6" viewBox="0 0 6 6"><path d="M1 .5 2.3 1.8 1.7 2.6Q2.6 4 3.6 4.4L4.3 3.8 5.5 5 4.7 5.7Q1.8 5 .3 1.3Z" fill="#5f6675"/></svg>&nbsp;&nbsp;+43 316 555 0192<br>
    <svg width="6" height="5" viewBox="0 0 6 5"><rect x=".3" y=".3" width="5.4" height="4.4" fill="none" stroke="#5f6675" stroke-width=".6"/><path d="M.3.3 3 2.6 5.7.3" fill="none" stroke="#5f6675" stroke-width=".6"/></svg>&nbsp;&nbsp;hello@veskarin.at
  </p>
  <div class="abs soc" style="left:347px"></div>
  <div class="abs soc" style="left:370px"></div>
  <div class="abs soc" style="left:392px"></div>
  <div class="abs soc" style="left:415px"></div>
  <div class="abs field" style="left:484px;top:1058px;width:81px;height:17px">Name</div>
  <div class="abs field" style="left:572px;top:1058px;width:81px;height:17px">Email</div>
  <div class="abs field" style="left:484px;top:1082px;width:169px;height:46px">Message</div>
  <div class="abs send">Send</div>
  <div class="abs f-rule"></div>
  <div class="abs copy">©2014 Veskarin - Health &amp; Beauty Center. All Rights Reserved</div>
</footer>
</body>
</html>
```